Business Card Design

Non-profit organization creating opportunities for:
Personal empowerment
Community Outreach
Healthier Life Choices
Body/Mind/Spirit Nourishment
Emotional Transformation
Charity & Network Opportunities
Everyday people making An extrodinary sufferance
All achieved from the Source within YOU.
Organization logo is the ying yang symbol with a small circle above it as if it were the head and the ying yang symbol was the body.  Also in side upper ying needs to be a heart and in the lower yang needs to be the letter C. This is very important as it came to me in a dream n the forming of this organization.  Color choice is open although a thought I hade was that the heart is red metallic foil (sine a red heart is the symbol of love)and the c is gold foil( the gifts of the 3 wise men and gold being one of them).a verticle card is preferred and logo as large as possible on it even if ying yang is made oval Ilook forward to the layouts and designs you can come up with.

Industry/Entity Type
Business
Contact Information for Business Card
Lumina Harbor. Org
Peter Galvany
Executive Director
Lumina harbor.peter@mailbrook.net
315-482-9063

```html
<!DOCTYPE html>
<html lang="en">
<head>
<meta charset="utf-8">
<title>Lumina Harbor – Business Card</title>
<link href="https://fonts.googleapis.com/css2?family=Didact+Gothic&family=Questrial&display=swap" rel="stylesheet">
<style>
  :root {
    --backdrop: #d9d4ce;
    --paper: #f4f4f2;
    --teal: #1e7f8a;
    --red: #b8202c;
    --navy: #2b3544;
    --tick: #3aa57a;
    --grey-text: #6d6f72;
  }
  * { box-sizing: border-box; margin: 0; padding: 0; }
  html, body { width: 1200px; height: 723px; overflow: hidden; }
  body {
    background: var(--backdrop);
    font-family: "Didact Gothic", "Century Gothic", sans-serif;
    position: relative;
  }
  .card {
    position: absolute;
    top: 82px;
    width: 320px;
    height: 560px;
    background: var(--paper);
    box-shadow: 0 6px 18px rgba(0,0,0,.18);
    overflow: hidden;
  }
  .card--back { left: 250px; }
  .card--front { left: 630px; }

  /* Back */
  .back-heading {
    position: absolute; top: 34px; right: 36px; width: 220px;
    text-align: center;
    font-family: "Questrial", sans-serif;
    font-variant: small-caps;
    color: var(--teal);
    font-size: 30px; line-height: 1.05; letter-spacing: 1px; font-weight: 700;
  }
  .offer-list {
    position: absolute; top: 160px; left: 30px; right: 24px;
    list-style: none;
    color: var(--grey-text);
    font-size: 17px; line-height: 1.32;
  }
  .offer-list li { position: relative; padding-left: 22px; }
  .offer-list li svg { position: absolute; left: 0; top: 5px; }
  .back-mark {
    position: absolute; bottom: 22px; right: 24px;
    display: flex; align-items: center; gap: 6px;
    color: var(--teal); font-size: 11px;
  }
  .back-mark .dot { width: 14px; height: 14px; border-radius: 50%; background: var(--navy); }

  /* Front */
  .logo-area {
    position: absolute; top: -14px; left: 30px;
    width: 260px; height: 260px; border-radius: 50%;
    background: var(--navy);
  }
  .org-name {
    position: absolute; top: 276px; left: 0; right: 0;
    text-align: center;
    font-family: "Questrial", sans-serif;
    font-variant: small-caps;
    color: var(--teal); font-size: 30px; font-weight: 700; letter-spacing: 1px;
  }
  .divider {
    position: absolute; top: 324px; left: 80px; right: 40px;
    border-top: 3px dotted var(--red);
  }
  .person-name {
    position: absolute; top: 340px; left: 38px;
    font-family: "Questrial", sans-serif;
    font-variant: small-caps;
    color: var(--teal); font-size: 34px; font-weight: 700; line-height: 1;
  }
  .person-title {
    position: absolute; top: 380px; left: 40px;
    color: var(--red); font-size: 15px; font-weight: 700;
  }
  .swoosh { position: absolute; left: 0; bottom: 0; }
  .contact-list {
    position: absolute; top: 430px; left: 96px;
    list-style: none; color: var(--teal); font-size: 14px; line-height: 1.55;
  }
  .contact-list li { display: flex; align-items: center; gap: 7px; }
  .contact-icon {
    width: 13px; height: 13px; border-radius: 50%;
    background: var(--red); color: #fff;
    font-size: 8px; line-height: 13px; text-align: center; font-weight: 700;
  }
</style>
</head>
<body>
  <section class="card card--back">
    <h2 class="back-heading">Creating opportunities for:</h2>
    <ul class="offer-list">
      <li><svg width="15" height="12" viewBox="0 0 15 12"><rect width="15" height="12" fill="none" stroke="#9aa" stroke-width="1"/><path d="M2 6l4 4 8-9" fill="none" stroke="var(--tick)" stroke-width="2.4"/></svg>Personal empowerment</li>
      <li><svg width="15" height="12" viewBox="0 0 15 12"><rect width="15" height="12" fill="none" stroke="#9aa" stroke-width="1"/><path d="M2 6l4 4 8-9" fill="none" stroke="var(--tick)" stroke-width="2.4"/></svg>Community Outreach</li>
      <li><svg width="15" height="12" viewBox="0 0 15 12"><rect width="15" height="12" fill="none" stroke="#9aa" stroke-width="1"/><path d="M2 6l4 4 8-9" fill="none" stroke="var(--tick)" stroke-width="2.4"/></svg>Healthier Life Choices</li>
      <li><svg width="15" height="12" viewBox="0 0 15 12"><rect width="15" height="12" fill="none" stroke="#9aa" stroke-width="1"/><path d="M2 6l4 4 8-9" fill="none" stroke="var(--tick)" stroke-width="2.4"/></svg>Body/Mind/Spirit Nourishment</li>
      <li><svg width="15" height="12" viewBox="0 0 15 12"><rect width="15" height="12" fill="none" stroke="#9aa" stroke-width="1"/><path d="M2 6l4 4 8-9" fill="none" stroke="var(--tick)" stroke-width="2.4"/></svg>Emotional Transformation</li>
      <li><svg width="15" height="12" viewBox="0 0 15 12"><rect width="15" height="12" fill="none" stroke="#9aa" stroke-width="1"/><path d="M2 6l4 4 8-9" fill="none" stroke="var(--tick)" stroke-width="2.4"/></svg>Charity &amp; Network Opportunities</li>
      <li><svg width="15" height="12" viewBox="0 0 15 12"><rect width="15" height="12" fill="none" stroke="#9aa" stroke-width="1"/><path d="M2 6l4 4 8-9" fill="none" stroke="var(--tick)" stroke-width="2.4"/></svg>Everyday people making an extrodinary sufferance</li>
      <li><svg width="15" height="12" viewBox="0 0 15 12"><rect width="15" height="12" fill="none" stroke="#9aa" stroke-width="1"/><path d="M2 6l4 4 8-9" fill="none" stroke="var(--tick)" stroke-width="2.4"/></svg>All achieved from the source within YOU</li>
    </ul>
    <div class="back-mark"><span class="dot"></span>Lumina Harbor</div>
  </section>

  <section class="card card--front">
    <div class="logo-area" role="img" aria-label="Lumina Harbor organisation mark area"></div>
    <h1 class="org-name">Lumina Harbor</h1>
    <div class="divider"></div>
    <p class="person-name">Peter Galvany</p>
    <p class="person-title">Executive Director</p>
    <svg class="swoosh" width="320" height="200" viewBox="0 0 320 200">
      <path d="M0 40 C 60 120, 180 175, 320 186 L320 196 C 175 186, 55 135, 0 58 Z" fill="var(--red)"/>
    </svg>
    <ul class="contact-list">
      <li><span class="contact-icon">W</span>luminaharbor.org</li>
      <li><span class="contact-icon">E</span>harbor.peter@mailbrook.net</li>
      <li><span class="contact-icon">C</span>315-482-9063</li>
    </ul>
  </section>
</body>
</html>
```